Album Artwork needed for House of Worship

We are a church called Lanternfield Church in New Jersey. We are a new church and just passed our two year mark.

This is our first album and it is entitled "Open Wide Skies" with a smaller text saying "Congregational Songs from Lanternfield Church".

Our album is based off of songs sung in our weekly services. It has a mix of contemporary christian, traditional and original songs.

We love creativity. Some of the album art we like are Brookvane, Marrow, Tinfolk, Rhea Vollmer's new album "Quiet Rising Tide"and Ember Harvest.

We are open to creativity outside of these examples.

In total we would need about 4 pages of designs for this project. One is the cover. The second is behind the cover. The third is the back of the album. The last is on the CD itself.

We have attached a word document with the specifics for what is to be on each page. We have also attached songs for you to listen and know our sound.

Thank you!

Target Market(s)

Church, Christians, Young Adults, Adults, College students

Industry/Entity Type

Church

Font styles to use
Decorative

Requirements
Must have
• Title: "Open Wide Skies" followed by "Congregational Songs from Lanternfield Church"
Nice to have
• We uploaded a shade of blue we would like to see on the album.
• Our church logo on the back of the album

```html
<!DOCTYPE html>
<html lang="en">
<head>
<meta charset="utf-8">
<title>Open Wide Skies – Album Credits</title>
<link href="https://fonts.googleapis.com/css2?family=Oswald:wght@300;400&display=swap" rel="stylesheet">
<style>
  :root {
    --sky-mauve: #8a7c82;
    --sky-grey: #7b7f80;
    --glow-warm: #e2a276;
    --glow-pink: #b56f7c;
    --field-teal: #3f9ea2;
    --field-blue: #3e4f98;
    --field-mist: #6fb4bc;
    --ink: #ffffff;
  }
  * { margin: 0; padding: 0; box-sizing: border-box; }
  html, body {
    width: 1200px; height: 1200px; overflow: hidden;
    background: var(--sky-mauve);
  }
  .back-panel {
    position: relative;
    width: 1200px; height: 1200px;
    overflow: hidden;
    font-family: "Oswald", "Arial Narrow", sans-serif;
    color: var(--ink);
  }
  .artwork { position: absolute; inset: 0; display: block; }
  .credits {
    position: absolute;
    left: 529px;
    top: 626px;
  }
  .credit-role {
    font-weight: 300;
    font-size: 35px;
    line-height: 1;
    letter-spacing: 0.42em;
    text-transform: uppercase;
    white-space: nowrap;
  }
  .credit-names {
    font-weight: 400;
    font-size: 24px;
    line-height: 1;
    margin-top: 16px;
    text-transform: uppercase;
    white-space: nowrap;
    letter-spacing: 0.01em;
  }
  .credit + .credit { margin-top: 40px; }
  .thanks {
    position: absolute;
    left: 0; right: 0;
    top: 1120px;
    text-align: center;
    font-weight: 400;
    font-size: 24px;
    text-transform: uppercase;
    white-space: nowrap;
  }
</style>
</head>
<body>
<main class="back-panel">
  <svg class="artwork" width="1200" height="1200" viewBox="0 0 1200 1200"
       role="img" aria-label="Tinted photograph of light beams over a tree line and open field at dusk">
    <defs>
      <linearGradient id="sky-field" x1="0" y1="0" x2="0" y2="1">
        <stop offset="0" stop-color="var(--sky-grey)"/>
        <stop offset="0.55" stop-color="var(--sky-mauve)"/>
        <stop offset="0.78" stop-color="var(--field-teal)"/>
        <stop offset="1" stop-color="var(--field-mist)"/>
      </linearGradient>
      <radialGradient id="warm-glow" cx="0.2" cy="0.35" r="0.55">
        <stop offset="0" stop-color="var(--glow-warm)" stop-opacity="0.9"/>
        <stop offset="0.5" stop-color="var(--glow-pink)" stop-opacity="0.55"/>
        <stop offset="1" stop-color="var(--glow-pink)" stop-opacity="0"/>
      </radialGradient>
      <radialGradient id="blue-shade" cx="0.1" cy="0.85" r="0.4">
        <stop offset="0" stop-color="var(--field-blue)" stop-opacity="0.7"/>
        <stop offset="1" stop-color="var(--field-blue)" stop-opacity="0"/>
      </radialGradient>
    </defs>
    <rect width="1200" height="1200" fill="url(#sky-field)"/>
    <rect width="1200" height="1200" fill="url(#warm-glow)"/>
    <rect width="1200" height="1200" fill="url(#blue-shade)"/>
  </svg>

  <section class="credits">
    <div class="credit">
      <h2 class="credit-role">Executive Producers:</h2>
      <p class="credit-names">Daniel Whitford + Ronald Whitford</p>
    </div>
    <div class="credit">
      <h2 class="credit-role">Produced By:</h2>
      <p class="credit-names">Jonah Whitford + Noel Whitford</p>
    </div>
    <div class="credit">
      <h2 class="credit-role">Recorded By:</h2>
      <p class="credit-names">Jonah Whitford + Noel Whitford</p>
    </div>
    <div class="credit">
      <h2 class="credit-role">Mixed + Mastered By:</h2>
      <p class="credit-names">Pell Ravena</p>
    </div>
  </section>

  <p class="thanks">Special thanks to the people of Lanternfield Church for their love and support in making all of this possible</p>
</main>
</body>
</html>
```